HIGH-END ANTI AGING START-UP NEEDS DOCUMENT/LETTERHEAD DESIGN!!!!

We are a high end anti-aging and health start-up catering to clients in Stamford and NYC. We just did a logo redesign and are now looking for a letter head design that we can use IN GOOGLE DOCS for marwickcaregroup.example clients. We are REALLY EXCITED to see what you can show us!!!!!!!! We need something sophisticated and MODERN! Thanks so much!

Target Market(s)

High end, boutique medical clients. Our clientele is fairly high profile and we need a sleek, sophisticated letter head to put on all of our marketing materials and medical forms as well.

Industry/Entity Type

Medical

Font styles to use
Serif
Sans Serif

Colors
0255a3
ffffff
00a990
1b1b1b
919191

Requirements
Must have
• Must have the logo and "Marwick Care Group" written somewhere. Must have our URL www.marwickcaregroup.example.
Nice to have
• office phone number (203) 555-0147
Should not have
• Colors outside of our logo colors + grey + black

```html
<!DOCTYPE html>
<html lang="en">
<head>
<meta charset="utf-8">
<title>Marwick Care Group – Letterhead</title>
<link rel="stylesheet" href="https://fonts.googleapis.com/css2?family=Libre+Baskerville:wght@700&family=Open+Sans:wght@400&display=swap">
<style>
  :root {
    --backdrop: #ececec;
    --paper: #ffffff;
    --brand-green: #00963f;
    --brand-blue: #4a7fe0;
    --ink: #1b1b1b;
    --icon-blue: #2f6fd1;
  }
  * { box-sizing: border-box; margin: 0; padding: 0; }
  html, body {
    width: 1200px;
    height: 1200px;
    overflow: hidden;
    background: var(--backdrop);
  }
  .canvas {
    position: relative;
    width: 1200px;
    height: 1200px;
  }
  .letterhead {
    position: absolute;
    left: 234px;
    top: 50px;
    width: 733px;
    height: 1100px;
    background: var(--paper);
  }
  .letterhead__brand {
    position: absolute;
    top: 120px;
    left: 0;
    right: 0;
    display: flex;
    justify-content: center;
    align-items: center;
    gap: 12px;
  }
  .brand-dot {
    width: 22px;
    height: 22px;
    border-radius: 50%;
    background: var(--brand-green);
  }
  .brand-name {
    font-family: "Libre Baskerville", Georgia, serif;
    font-weight: 700;
    font-size: 22px;
    letter-spacing: 0.5px;
    color: var(--brand-blue);
  }
  .letterhead__rule {
    position: absolute;
    top: 1013px;
    height: 7px;
  }
  .letterhead__rule--green {
    left: -2px;
    width: 366px;
    background: var(--brand-green);
    clip-path: polygon(0 0, 100% 0, 99% 100%, 0 100%);
  }
  .letterhead__rule--blue {
    left: 371px;
    right: -2px;
    top: 1015px;
    height: 6px;
    background: var(--brand-blue);
    clip-path: polygon(0 0, 100% 0, 100% 100%, 1% 100%);
  }
  .letterhead__contact {
    position: absolute;
    top: 1053px;
    left: 0;
    right: 0;
    display: flex;
    justify-content: center;
    gap: 28px;
    font-family: "Open Sans", Arial, sans-serif;
    font-size: 11px;
    color: var(--ink);
  }
  .contact-item {
    display: flex;
    align-items: center;
    gap: 10px;
  }
  .contact-icon { width: 10px; height: 10px; }
</style>
</head>
<body>
<main class="canvas">
  <section class="letterhead">
    <header class="letterhead__brand">
      <span class="brand-dot" aria-hidden="true"></span>
      <span class="brand-name">Marwick Care Group</span>
    </header>

    <div class="letterhead__rule letterhead__rule--green"></div>
    <div class="letterhead__rule letterhead__rule--blue"></div>

    <footer class="letterhead__contact">
      <span class="contact-item">
        <svg class="contact-icon" viewBox="0 0 10 10" aria-hidden="true">
          <path d="M3 0.5 L4.5 2.5 L3.5 3.5 Q4.5 6 6.5 6.8 L7.5 5.8 L9.5 7.3 L8.3 9 Q3 8.5 1 1.7 Z" fill="var(--icon-blue)"/>
        </svg>
        (203) 555-0147
      </span>
      <span class="contact-item">
        <svg class="contact-icon" viewBox="0 0 10 10" aria-hidden="true">
          <g fill="none" stroke="var(--icon-blue)" stroke-width="0.8">
            <circle cx="5" cy="5" r="4.2"/>
            <ellipse cx="5" cy="5" rx="1.9" ry="4.2"/>
            <line x1="0.8" y1="5" x2="9.2" y2="5"/>
          </g>
        </svg>
        www.marwickcaregroup.example
      </span>
    </footer>
  </section>
</main>
</body>
</html>
```